Flyer for Cool Choir Concert

8.5x11 color flyer, to get people to attend excellent concert

Requirements
Should not have
• I don't like a lot of musical symbols incorporated into the design.

```html
<!DOCTYPE html>
<html lang="en">
<head>
<meta charset="utf-8">
<title>Cantabile – War and Peace</title>
<link rel="stylesheet" href="https://fonts.googleapis.com/css2?family=Tinos:wght@400;700&family=Stardos+Stencil:wght@700&display=swap">
<style>
  :root {
    --purple: #4f1f74;
    --gold-text: #e8bb4d;
    --gold-pill: #c68b3f;
    --gold-pill-light: #dba55a;
    --cream: #fbedc4;
    --ink: #2a2024;
    --grey-title: #555055;
    --lavender: #e3d6f5;
    --page-bg: #e4e4e4;
    --white: #ffffff;
  }
  * { box-sizing: border-box; margin: 0; padding: 0; }
  html, body { width: 707px; height: 1200px; overflow: hidden; background: var(--page-bg); }
  body { position: relative; font-family: "Tinos", "Times New Roman", serif; }

  .flyer {
    position: absolute; left: 0; top: 100px; width: 707px; height: 1000px;
    background: var(--white); overflow: hidden;
    box-shadow: 0 4px 14px rgba(0,0,0,.25);
  }
  .header-band { position: absolute; left: 0; top: 0; width: 707px; height: 175px; }
  .header-text { position: absolute; left: 0; top: 16px; width: 100%; text-align: center; }
  .ensemble-name { color: var(--white); font-weight: 700; font-size: 36px; letter-spacing: .5px; }
  .ensemble-tagline { color: var(--gold-text); font-size: 22px; line-height: 28px; margin-top: 4px; }

  .presents { position: absolute; top: 168px; width: 100%; text-align: center;
    font-weight: 700; font-size: 33px; color: var(--grey-title); letter-spacing: .5px; }
  .concert-title { position: absolute; top: 202px; width: 100%; text-align: center;
    font-family: "Stardos Stencil", "Tinos", serif; font-weight: 700; font-size: 60px;
    color: var(--purple); letter-spacing: 2px; line-height: 64px; }
  .concert-blurb { position: absolute; top: 272px; left: 95px; width: 517px; text-align: center;
    font-size: 13.5px; line-height: 16px; color: var(--ink); }

  .choir-photo {
    position: absolute; left: 86px; top: 334px; width: 536px; height: 306px;
    border: 8px solid var(--white); box-shadow: 0 2px 8px rgba(0,0,0,.35);
    background: linear-gradient(180deg, #d9a63e 0%, #e5b85a 35%, #3a3030 58%, #8a6a4a 80%, #b38b62 100%);
  }

  .footer-wave { position: absolute; left: 0; top: 650px; width: 707px; height: 350px; }

  .venue { position: absolute; left: 0; top: 806px; width: 355px; text-align: center; }
  .venue-name { color: var(--purple); font-size: 38px; font-weight: 400; letter-spacing: 1px; line-height: 40px; }
  .venue-address { margin-top: 26px; font-weight: 700; font-size: 17px; line-height: 24px; color: var(--ink); }
  .web-row { margin: 12px auto 0; width: 310px; display: flex; align-items: center; gap: 8px; }
  .web-row::before, .web-row::after { content: ""; flex: 1; height: 1px; background: var(--grey-title); }
  .web-address { color: var(--purple); font-weight: 700; font-size: 19px; }
  .childcare { font-size: 11px; font-weight: 700; color: var(--ink); margin-top: 2px; }

  .column-rule { position: absolute; left: 355px; top: 755px; width: 1px; height: 222px; background: #7b6f6b; }

  .dates { position: absolute; left: 373px; top: 750px; width: 310px; }
  .date-pill {
    height: 34px; margin-bottom: 14px; border-radius: 17px 12px 17px 12px;
    background: linear-gradient(90deg, var(--gold-pill) 0%, var(--gold-pill-light) 50%, var(--gold-pill) 100%);
    color: var(--ink); font-weight: 700; font-size: 18px; line-height: 34px; text-align: center;
  }
  .ticket-note { position: absolute; left: 373px; top: 843px; width: 310px; text-align: center;
    font-weight: 700; font-size: 13px; line-height: 17px; color: var(--ink); }
  .price-ticket { position: absolute; left: 436px; top: 885px; width: 196px; height: 96px; }
  .price-list { position: absolute; left: 436px; top: 891px; width: 196px; text-align: center;
    color: var(--lavender); font-size: 22px; line-height: 27px; }
</style>
</head>
<body>
  <main class="flyer">
    <svg class="header-band" viewBox="0 0 707 175" aria-hidden="true">
      <polygon fill="#d9d6dc" points="0,0 707,0 707,150 680,160 650,148 620,164 590,152 555,166 520,150 490,162 455,148 420,164 385,152 350,166 315,150 280,162 245,148 210,166 175,152 140,164 105,150 70,166 35,152 0,164"/>
      <polygon fill="var(--purple)" points="0,0 707,0 707,140 680,150 650,138 620,154 590,142 555,156 520,140 490,152 455,138 420,154 385,142 350,156 315,140 280,152 245,138 210,156 175,142 140,154 105,140 70,156 35,142 0,154"/>
    </svg>
    <header class="header-text">
      <h1 class="ensemble-name">CANTABILE</h1>
      <p class="ensemble-tagline">Voices of the High Desert Daniel Hartwell,<br>Artistic Director</p>
    </header>

    <p class="presents">PRESENTS</p>
    <h2 class="concert-title">WAR AND PEACE</h2>
    <p class="concert-blurb">Join the singers of Cantabile as we perform music borne out of warfare and conflict, and music that celebrates peace and love. Featuring music of Owen Ashby, Ruth Kessler, Leo Marsh, Clara Dunmore, and others.</p>

    <div class="choir-photo" role="img" aria-label="Photo of the choir in black concert dress singing on risers before a gold curtain, with the conductor at a grand piano"></div>

    <svg class="footer-wave" viewBox="0 0 707 350" aria-hidden="true">
      <path fill="var(--cream)" d="M0,95 C150,55 330,75 470,60 C580,48 650,40 707,70 L707,350 L0,350 Z"/>
      <path fill="var(--purple)" d="M0,60 C110,95 300,80 460,45 C570,22 650,25 707,60 L707,75 C650,45 580,45 470,65 C330,95 150,110 0,95 Z"/>
    </svg>

    <section class="venue">
      <p class="venue-name">CANTABILE</p>
      <p class="venue-address">St. Brendan's Community Church<br>1840 Canyon Street NE Albuquerque</p>
      <div class="web-row"><span class="web-address">www.cantabile-choir.com</span></div>
      <p class="childcare">Complimentary childcare provided at both performances.</p>
    </section>

    <div class="column-rule"></div>

    <section class="dates">
      <p class="date-pill">Saturday, October 13 at 7:30pm</p>
      <p class="date-pill">Sunday, October 14 at 3:00pm</p>
    </section>
    <p class="ticket-note">Tickets Available Online<br>and at The Door</p>

    <svg class="price-ticket" viewBox="0 0 196 96" aria-hidden="true">
      <path fill="var(--purple)" d="M10,0 H186 A10,10 0 0 0 196,10 V86 A10,10 0 0 0 186,96 H10 A10,10 0 0 0 0,86 V10 A10,10 0 0 0 10,0 Z"/>
      <path fill="none" stroke="var(--lavender)" stroke-width="1" d="M14,5 H182 A9,9 0 0 0 191,14 V82 A9,9 0 0 0 182,91 H14 A9,9 0 0 0 5,82 V14 A9,9 0 0 0 14,5 Z"/>
    </svg>
    <div class="price-list">
      <p>General $20</p>
      <p>Seniors $15</p>
      <p>Students $10</p>
    </div>
  </main>
</body>
</html>
```